Greek Yogurt Design

Design Brief – Premium Greek Yogurt Line (150g Pot)
Background
We are a small-to-medium dairy producer launching a new premium Greek yogurt range. This line will come in slightly larger pots than our standard yogurts, and we are targeting an upmarket clientele with a higher price point.
Product Details
Product: Greek Yogurt (fruit on the bottom, yogurt on top)
Flavours:
Natural
Strawberry
Forest Fruit
Peach & Apricot
Vanilla
Mango
Weight: 150g
Kosher Certification: 2 logos must be applied neatly (logos provided).
Lid: Standard universal lid (not flavour-specific).
Design Style
Clean, elegant, and premium feel (avoid clutter).
Should stand out as sophisticated compared to our standard range.
Visual hierarchy:
Brand & product type (Greek Yogurt) should be clear.
Flavour indicated with subtle but distinct cues (colour palette, fruit illustration/photography).
“Fruit on the bottom” message should be communicated simply.
Premium cues: minimalist typography, restrained colour palette, elegant fruit imagery.
References / Inspiration
Velmora Yogurt
– clean, bold, dairy-traditional.
Brask Dairy Greek Style
– natural, elegant design.
Lunaro Greek Yogurt
– modern, colourful yet clean.
Deliverables
Pot sleeve / pot design (to wrap around container).
Must work across all flavours with colour/flavour variation.
Space for universal lid (do not design individual lids).
Application of 2 kosher logos in a balanced way.
Updates
Industry/Entity Type
Dairy
Colors
Designer to choose colors to be used in the design.
Look and feel
Each slider illustrates characteristics of the customer's brand and the style your logo design should communicate.

```html
<!DOCTYPE html>
<html lang="en">
<head>
<meta charset="UTF-8">
<title>Melkaro Greek Yogurt – Strawberry Pot Sleeve</title>
<link href="https://fonts.googleapis.com/css2?family=Fredoka:wght@500;600&family=Lobster&display=swap" rel="stylesheet">
<style>
  :root {
    --page: #ffffff;
    --sleeve-top: #f6d3d3;
    --sleeve-mid: #fbeeee;
    --sleeve-bottom: #f3c7c8;
    --rim-top: #f1c4c4;
    --rim-bottom: #f8dcdc;
    --brand-green: #3aa53f;
    --berry-red: #d4232e;
    --berry-light: #ef5058;
    --berry-deep: #b3121d;
    --ink: #2a2a2a;
  }
  * { box-sizing: border-box; margin: 0; padding: 0; }
  html, body {
    width: 1200px;
    height: 900px;
    overflow: hidden;
    background: var(--page);
  }
  .canvas {
    position: relative;
    width: 1200px;
    height: 900px;
    display: flex;
    align-items: center;
    justify-content: center;
  }
  .sleeve {
    position: relative;
    width: 640px;
    height: 800px;
    border-radius: 18px;
    background: linear-gradient(180deg, var(--sleeve-top) 0%, var(--sleeve-mid) 30%, var(--sleeve-mid) 55%, var(--sleeve-bottom) 100%);
    overflow: hidden;
  }
  .sleeve-rim {
    position: absolute;
    left: 0; right: 0; top: 0;
    height: 70px;
    background: linear-gradient(180deg, var(--rim-top), var(--rim-bottom));
    border-bottom: 2px solid rgba(200, 140, 140, 0.25);
  }
  .brand-lockup {
    position: absolute;
    top: 120px;
    left: 0; right: 0;
    text-align: center;
  }
  .brand-name {
    font-family: 'Fredoka', sans-serif;
    font-weight: 600;
    font-size: 104px;
    line-height: 1;
    color: var(--brand-green);
    letter-spacing: 1px;
  }
  .brand-tagline {
    margin-top: 6px;
    font-family: 'Fredoka', sans-serif;
    font-weight: 600;
    font-size: 26px;
    color: var(--brand-green);
    letter-spacing: 2px;
  }
  .product-type {
    position: absolute;
    top: 330px;
    left: 0; right: 0;
    text-align: center;
    font-family: 'Fredoka', sans-serif;
    font-weight: 600;
    font-size: 100px;
    line-height: 0.95;
    color: var(--brand-green);
    letter-spacing: 1px;
  }
  .flavour-block {
    position: absolute;
    top: 560px;
    left: 130px; right: 130px;
    text-align: center;
  }
  .flavour-rule {
    height: 3px;
    background: var(--berry-red);
    border-radius: 2px;
  }
  .flavour-name {
    margin-top: 12px;
    font-family: 'Lobster', cursive;
    font-size: 54px;
    line-height: 1.05;
    color: var(--berry-red);
  }
  .flavour-note {
    margin: 2px 0 12px;
    font-family: 'Lobster', cursive;
    font-size: 28px;
    line-height: 1.1;
    color: var(--ink);
  }
  .fruit-art {
    position: absolute;
    background: radial-gradient(circle at 40% 40%, var(--berry-light), var(--berry-red) 60%, var(--berry-deep));
    border-radius: 48% 48% 50% 50% / 40% 40% 60% 60%;
  }
  .fruit-left-top  { left: 20px;  top: 290px; width: 100px; height: 140px; }
  .fruit-left-low  { left: 26px;  top: 470px; width: 80px;  height: 220px; }
  .fruit-right-top { right: 26px; top: 270px; width: 100px; height: 150px; }
  .fruit-right-low { right: 28px; top: 460px; width: 80px;  height: 230px; }
  .fruit-bottom    { left: 270px; bottom: -30px; width: 140px; height: 110px; }
</style>
</head>
<body>
  <main class="canvas">
    <section class="sleeve">
      <div class="sleeve-rim"></div>

      <div class="brand-lockup">
        <div class="brand-name">Melkaro</div>
        <div class="brand-tagline">Pure Dairy Craft</div>
      </div>

      <h1 class="product-type">GREEK<br>YOGURT</h1>

      <div class="flavour-block">
        <div class="flavour-rule"></div>
        <div class="flavour-name">Strawberry</div>
        <div class="flavour-note">on the Bottom</div>
        <div class="flavour-rule"></div>
      </div>

      <div class="fruit-art fruit-left-top" role="img" aria-label="Illustration of a halved strawberry"></div>
      <div class="fruit-art fruit-left-low" role="img" aria-label="Illustration of a whole strawberry"></div>
      <div class="fruit-art fruit-right-top" role="img" aria-label="Illustration of a halved strawberry"></div>
      <div class="fruit-art fruit-right-low" role="img" aria-label="Illustration of a whole strawberry"></div>
      <div class="fruit-art fruit-bottom" role="img" aria-label="Illustration of a halved strawberry with leaves"></div>
    </section>
  </main>
</body>
</html>
```